marcello's mobile mechanic

a business card that will get attention from clients
- name of the business: M'S MOBILE MECHANIC
- we currently do not have a logo and do not need one at the moment, happy for the designers to just put the business name on the card using appropriate fonts

Target Market(s)

low cost mobile repairs

Industry/Entity Type

Business

Contact Information for Business Card

attracts customers

Font styles to use
Sans Serif

Colors
0255a3
fbee3d
000000

Requirements
Must have
• (555) 314-7829
• Marcello Tiernan
• for lower income target market
Nice to have
• "we save you money"
• Easy to read
Should not have
• nothing comes to mind

```html
<!DOCTYPE html>
<html lang="en">
<head>
<meta charset="utf-8">
<title>M'S Mobile Mechanic – Business Card</title>
<link rel="stylesheet" href="https://fonts.googleapis.com/css2?family=Montserrat:wght@400;500;700&display=swap">
<style>
  :root {
    --brand-blue: #0255a3;
    --ink: #000000;
    --paper: #ffffff;
    --backdrop: #dcdcdc;
    --pattern-blue: #0452a3;
  }
  html, body {
    margin: 0;
    padding: 0;
    overflow: hidden;
  }
  body {
    width: 1200px;
    height: 1200px;
    background: var(--backdrop);
    position: relative;
    font-family: "Montserrat", sans-serif;
  }
  .card {
    position: absolute;
    width: 756px;
    height: 432px;
    box-sizing: border-box;
    overflow: hidden;
  }
  .card--front {
    left: 350px;
    top: 138px;
    background: var(--paper);
  }
  .card--back {
    left: 95px;
    top: 630px;
    background: var(--brand-blue);
  }
  .business-name {
    position: absolute;
    right: 382px;
    top: 210px;
    margin: 0;
    font-weight: 700;
    font-size: 23px;
    color: var(--brand-blue);
    white-space: nowrap;
    letter-spacing: 0.2px;
  }
  .divider {
    position: absolute;
    left: 400px;
    top: 166px;
    width: 2px;
    height: 100px;
    background: var(--ink);
  }
  .contact {
    position: absolute;
    left: 433px;
    top: 184px;
  }
  .contact__name {
    margin: 0;
    font-weight: 500;
    font-size: 27px;
    line-height: 32px;
    color: var(--ink);
    white-space: nowrap;
  }
  .contact__phone {
    margin: 4px 0 0;
    display: flex;
    align-items: center;
    gap: 14px;
    font-weight: 500;
    font-size: 19px;
    color: var(--ink);
    letter-spacing: 0.6px;
    white-space: nowrap;
  }
  .contact__icon {
    width: 20px;
    height: 20px;
    fill: var(--brand-blue);
  }
  .tool-pattern {
    position: absolute;
    inset: 0;
    background: var(--pattern-blue);
  }
  .tagline {
    position: absolute;
    left: 0;
    right: 0;
    top: 196px;
    margin: 0;
    text-align: center;
    font-weight: 500;
    font-size: 32px;
    line-height: 40px;
    color: var(--paper);
    white-space: nowrap;
  }
</style>
</head>
<body>
  <section class="card card--front" aria-label="Business card front">
    <h1 class="business-name">M'S MOBILE MECHANIC</h1>
    <div class="divider"></div>
    <div class="contact">
      <p class="contact__name">Marcello Tiernan</p>
      <p class="contact__phone">
        <svg class="contact__icon" viewBox="0 0 24 24" aria-hidden="true">
          <path d="M6.6 10.8c1.4 2.8 3.8 5.1 6.6 6.6l2.2-2.2c.3-.3.7-.4 1-.2 1.1.4 2.3.6 3.6.6.6 0 1 .4 1 1V20c0 .6-.4 1-1 1C10.6 21 3 13.4 3 4c0-.6.4-1 1-1h3.5c.6 0 1 .4 1 1 0 1.3.2 2.5.6 3.6.1.3 0 .7-.2 1L6.6 10.8z"/>
        </svg>
        (555) 314-7829
      </p>
    </div>
  </section>

  <section class="card card--back" aria-label="Business card back">
    <div class="tool-pattern" role="img" aria-label="Scattered pattern of tool, gear, nut and phone icons in darker blue"></div>
    <p class="tagline">WE SAVE YOU MONEY</p>
  </section>
</body>
</html>
```